Eye catching business card

2 sided
Black background with logo in color on one side along with the words "Proudly serving the commercial and defense industries since 1975"
2nd side to contain contact information (see attached current business card) and "Waterjet, Composite, Precision Machining and Clean Room Manufacturing" with a very faint watermark of a waving USA Flag in the back ground.
Remove the "est. 195" from the current logo design

```html
<!DOCTYPE html>
<html lang="en">
<head>
<meta charset="utf-8">
<title>Meridian Fabrication – Business Card</title>
<link rel="stylesheet" href="https://fonts.googleapis.com/css2?family=Barlow:wght@500;600;700&display=swap">
<style>
  :root {
    --page-bg: #e3e4e6;
    --ink-blue: #3a52a6;
    --mid-blue: #5a7bbd;
    --bright-blue: #24ace2;
    --pale-blue: #86c4ec;
    --back-black: #050608;
    --white: #ffffff;
    --flag-blue: #dcdeee;
    --flag-peach: #f6e6dc;
  }
  * { margin: 0; padding: 0; box-sizing: border-box; }
  html, body {
    width: 1200px; height: 1200px; overflow: hidden;
    background: var(--page-bg);
    font-family: "Barlow", Arial, sans-serif;
  }
  .card {
    position: absolute; left: 225px; width: 750px; height: 417px; overflow: hidden;
  }
  .card--front { top: 122px; background: var(--white); color: var(--ink-blue); }
  .card--back { top: 638px; background: var(--back-black); }

  .flag-backdrop {
    position: absolute; inset: 0;
    background: linear-gradient(115deg, var(--flag-blue) 0%, #e8e9f2 35%, #f7f2ef 55%, var(--flag-peach) 78%, #fbf3ee 100%);
  }
  .corner-shapes { position: absolute; inset: 0; }

  .person-icon { position: absolute; left: 414px; top: 54px; width: 50px; height: 58px; }
  .holder-name {
    position: absolute; right: 67px; top: 50px;
    font-size: 31px; font-weight: 700; line-height: 1;
  }
  .holder-role {
    position: absolute; right: 67px; top: 93px;
    font-size: 21px; font-weight: 600; line-height: 1;
  }
  .holder-rule {
    position: absolute; left: 414px; top: 121px; width: 271px; height: 2px;
    background: var(--ink-blue);
  }
  .holder-contact {
    position: absolute; right: 67px; top: 134px; text-align: right;
    font-size: 18px; font-weight: 500; line-height: 24px;
  }
  .holder-contact strong { font-weight: 700; font-size: 20px; letter-spacing: .5px; }

  .company-name {
    position: absolute; left: 0; right: 0; top: 224px; text-align: center;
    font-size: 27px; font-weight: 600; line-height: 1;
  }
  .company-services {
    position: absolute; left: 0; right: 0; top: 263px; text-align: center;
    font-size: 18px; font-weight: 600; line-height: 1;
  }
  .company-contacts {
    position: absolute; left: 196px; top: 300px; list-style: none;
    font-size: 15px; font-weight: 500; line-height: 29px;
  }
  .company-contacts li span { margin-right: 14px; }
  .company-contacts li span::before {
    content: "\25B6"; font-size: 9px; margin-right: 8px; vertical-align: 2px;
  }

  .brand { position: absolute; left: 72px; top: 45px; display: flex; align-items: center; gap: 18px; }
  .brand-square { width: 130px; height: 130px; background: var(--bright-blue); }
  .brand-name { color: var(--bright-blue); font-weight: 600; line-height: 1; }
  .brand-name .brand-main { display: block; font-size: 66px; letter-spacing: 1px; }
  .brand-name .brand-sub { display: block; font-size: 22px; letter-spacing: 9px; margin-top: 8px; padding-left: 4px; }

  .back-tagline {
    position: absolute; left: 0; right: 0; top: 293px; text-align: center;
    color: var(--white); font-weight: 600; font-size: 22px; line-height: 31px;
  }
  .back-tagline strong { font-weight: 700; font-size: 25px; }
</style>
</head>
<body>

<section class="card card--front">
  <div class="flag-backdrop" role="img" aria-label="Very faint waving USA flag watermark"></div>

  <svg class="corner-shapes" viewBox="0 0 750 417" aria-hidden="true">
    <polygon points="0,213 41,254 0,295" fill="var(--mid-blue)"/>
    <polygon points="0,275 70,322 0,393" fill="var(--ink-blue)"/>
    <polygon points="750,213 709,254 750,295" fill="var(--mid-blue)"/>
    <polygon points="750,275 680,322 750,393" fill="var(--ink-blue)"/>
  </svg>

  <svg class="person-icon" viewBox="0 0 51 59" aria-hidden="true">
    <ellipse cx="25.5" cy="17" rx="13" ry="17" fill="var(--ink-blue)"/>
    <path d="M0 59 V50 Q2 38 17 36 H34 Q49 38 51 50 V59 Z" fill="var(--ink-blue)"/>
  </svg>

  <h1 class="holder-name">Dana Whitfield</h1>
  <p class="holder-role">President</p>
  <div class="holder-rule"></div>
  <p class="holder-contact">office: <strong>555-310-4420</strong><br>dana@meridianfab.com</p>

  <h2 class="company-name">Meridian Fabrication, Inc.</h2>
  <p class="company-services">Waterjet, Composite, Precision Machining &amp; Clean Room Manufacturing</p>
  <ul class="company-contacts">
    <li><span>Phone: 555-310-4420</span><span>Fax: 555-310-4441</span></li>
    <li><span>info@meridianfab.com</span><span>www.meridianfab.com</span></li>
    <li><span>412 Harlow Mill Rd. Glen Ridge, PA 17310</span></li>
  </ul>
</section>

<section class="card card--back">
  <svg class="corner-shapes" viewBox="0 0 750 417" aria-hidden="true">
    <polygon points="0,287 41,327 0,368" fill="var(--pale-blue)"/>
    <polygon points="0,197 70,268 0,310" fill="var(--bright-blue)"/>
    <polygon points="750,287 709,327 750,368" fill="var(--pale-blue)"/>
    <polygon points="750,197 680,268 750,310" fill="var(--bright-blue)"/>
  </svg>

  <div class="brand">
    <div class="brand-square"></div>
    <p class="brand-name"><span class="brand-main">MERIDIAN</span><span class="brand-sub">FABRICATION INC</span></p>
  </div>

  <p class="back-tagline">Proudly serving the commercial and defense industries<br><strong>since 1975</strong></p>
</section>

</body>
</html>
```